Business card design needed

Our company background is that we provides transfers to and from the airport, social & corporate events, weddings.
We are also available for charter for birthday party, wine tastings, concerts, anniversary, school balls etc.
Our business cards have to reflect that we have a professional company, they are our first contact and have to stand out from the other 'players' in the market.

Industry/Entity Type

School

Contact Information for Business Card

BRISTEL QDF, Laurent & Marisol, mob: 0427 381 594, PO Box 287, Tarrowin WA 6311, ABN 52 914 603 278, Lic 7169/5804,

Requirements
Must have
• Telephone number: 0427 381 594
Website: www.BRISTELQDF.com.au
postal address: PO Box 287, Tarrowin WA 6311
Licences: Lic 7169/5804

***If using the new photo (one with the bus and buildings behind it), if possible can the buildings be cropped out. Thanks
Nice to have
• would be nice to have the pics of the vehicle(s), preferred the Pel on the card but not too fussed.
Should not have
• Picture of vehicle we don't have in our fleet. (We ONLY have the Pellics and Rendak Ovaro mini bus)

```html
<!DOCTYPE html>
<html lang="en">
<head>
<meta charset="utf-8">
<title>BRISTEL QDF – Business Card</title>
<link href="https://fonts.googleapis.com/css2?family=Open+Sans:wght@400;600;700&display=swap" rel="stylesheet">
<style>
  :root {
    --page-bg: #e4e1dc;
    --card-black: #0c0c0c;
    --card-sheen: #2a2a2a;
    --text-white: #ffffff;
    --text-soft: #d8d8d8;
    --text-muted: #c4c4c4;
    --photo-sky: #c9d3d8;
    --photo-leaf: #6f7f5a;
    --photo-silver: #b9b7b0;
    --photo-deck: #8a6a4c;
  }
  html, body {
    margin: 0;
    width: 1200px;
    height: 964px;
    overflow: hidden;
    background: var(--page-bg);
    font-family: "Open Sans", Arial, sans-serif;
  }
  .card {
    position: absolute;
    left: 100px;
    top: 196px;
    width: 1000px;
    height: 572px;
    background: linear-gradient(160deg, var(--card-sheen) 0%, var(--card-black) 45%, var(--card-black) 100%);
    box-shadow: 0 12px 30px rgba(0,0,0,0.35);
    overflow: hidden;
  }
  .vehicle-photo {
    position: absolute;
    inset: 0;
    background:
      radial-gradient(ellipse 40% 45% at 62% 30%, var(--photo-silver) 0%, rgba(185,183,176,0.6) 55%, transparent 80%),
      linear-gradient(135deg, var(--photo-leaf) 0%, var(--photo-sky) 40%, var(--photo-sky) 60%, var(--photo-deck) 100%);
    clip-path: polygon(340px 0, 1000px 0, 1000px 140px, 560px 290px, 340px 290px);
  }
  .identity {
    position: absolute;
    left: 56px;
    top: 240px;
    color: var(--text-white);
  }
  .company-name {
    margin: 0;
    font-size: 44px;
    font-weight: 700;
    letter-spacing: 0.5px;
    line-height: 52px;
  }
  .owners {
    margin: 0;
    font-size: 32px;
    line-height: 44px;
    color: var(--text-soft);
  }
  .mobile {
    margin: 0;
    font-size: 30px;
    line-height: 42px;
    color: var(--text-soft);
  }
  .postal {
    position: absolute;
    left: 110px;
    top: 396px;
    margin: 0;
    font-size: 18px;
    line-height: 25px;
    color: var(--text-muted);
    font-style: normal;
    white-space: nowrap;
  }
  .services {
    position: absolute;
    left: 320px;
    bottom: 38px;
    margin: 0;
    font-size: 14px;
    line-height: 24px;
    color: var(--text-white);
    white-space: nowrap;
  }
</style>
</head>
<body>
  <div class="card">
    <div class="vehicle-photo" role="img" aria-label="Photo of a silver Pel sedan parked beside trees"></div>
    <div class="identity">
      <h1 class="company-name">BRISTEL QDF</h1>
      <p class="owners">Laurent &amp; Marisol</p>
      <p class="mobile">mob: 0427 381 594</p>
    </div>
    <address class="postal">
      PO Box 287,<br>
      Tarrowin WA 6311,<br>
      ABN 52 914 603 278<br>
      Lic 7169/5804
    </address>
    <p class="services">
      Transfers to and from the airport, social &amp; corporate events, weddings<br>
      charter for birthday party, wine tastings, concerts, anniversary, school balls etc.
    </p>
  </div>
</body>
</html>
```